Create a banner for a Gmail email signature

We need a graphic design to use in a solicitor's email signature. The banner will incorporate a head shot of the solicitor as well as the law firm's logo and contact details. The solicitor's photo and law firm's logo are uploaded in the task.

```html
<!DOCTYPE html>
<html lang="en">
<head>
<meta charset="utf-8">
<title>Email Signature – Harbour Lane Law</title>
<link rel="stylesheet" href="https://fonts.googleapis.com/css2?family=Montserrat:wght@300;400&family=Source+Sans+3:wght@400&display=swap">
<style>
  :root {
    --plum: #8e1a57;
    --ink: #1d1d1f;
    --white: #ffffff;
    --stage: #dfe4ed;
    --photo-light: #d9c3b0;
    --photo-dark: #3b4660;
  }
  * { box-sizing: border-box; margin: 0; padding: 0; }
  html, body { width: 1200px; height: 1200px; overflow: hidden; }
  body {
    position: relative;
    background: var(--stage);
    font-family: "Montserrat", sans-serif;
    font-weight: 300;
    color: var(--ink);
  }
  .sheet-header {
    position: absolute; left: 0; top: 0; width: 1200px; height: 181px;
    background: var(--white);
  }
  .sheet-title {
    position: absolute; left: 0; width: 1200px; top: 76px;
    text-align: center;
    font-family: "Source Sans 3", sans-serif; font-weight: 400;
    font-size: 36px; line-height: 1; color: var(--plum);
  }
  .signature {
    position: absolute; left: 178px; width: 845px; height: 254px;
    background: var(--white);
    box-shadow: 0 22px 26px -18px rgba(40, 50, 80, 0.35);
  }
  .signature--split { top: 255px; }
  .signature--banner { top: 547px; }
  .signature--footer { top: 839px; }

  .abs { position: absolute; line-height: 1; white-space: nowrap; }
  .headshot {
    position: absolute; border-radius: 50%;
    background: radial-gradient(circle at 50% 42%, var(--photo-light) 0 38%, #b89a86 55%, var(--photo-dark) 100%);
  }
  .person-name { color: var(--plum); font-weight: 400; font-size: 28px; letter-spacing: 0.5px; }
  .person-role { color: var(--ink); font-weight: 400; font-size: 19px; letter-spacing: 0.6px; }
  .contact { font-size: 20px; color: var(--ink); }
  .contact-icon { position: absolute; fill: var(--plum); }
  .centered { text-align: center; }

  .brand-panel {
    position: absolute; left: 529px; top: 0; width: 316px; height: 254px;
    background: var(--plum);
  }
  .brand-band {
    position: absolute; left: 0; top: 190px; width: 845px; height: 64px;
    background: var(--plum);
  }
  .brand-rule {
    position: absolute; left: 0; top: 190px; width: 845px; height: 8px;
    background: var(--plum);
  }
  .brand-name {
    font-family: "Source Sans 3", sans-serif; font-weight: 400;
    font-size: 28px; letter-spacing: -0.3px;
  }
  .web { font-size: 18px; letter-spacing: 0.3px; }
  .on-plum { color: var(--white); }
  .in-plum { color: var(--plum); }
  .social { position: absolute; width: 24px; height: 24px; border-radius: 50%; }
  .social--light { background: var(--white); }
  .social--plum { background: var(--plum); }
</style>
</head>
<body>
  <header class="sheet-header">
    <h1 class="sheet-title abs">EMAIL SIGNATURE</h1>
  </header>

  <!-- Split layout: contact left, brand panel right -->
  <section class="signature signature--split">
    <div class="headshot" role="img" aria-label="Head shot of the solicitor" style="left:29px;top:51px;width:154px;height:154px;"></div>
    <div class="person-name abs" style="left:214px;top:44px;">YOUR NAME</div>
    <div class="person-role abs" style="left:214px;top:82px;">LAWYER</div>

    <svg class="contact-icon" style="left:210px;top:142px;" width="19" height="13" viewBox="0 0 19 13" aria-hidden="true"><path d="M0 0h19v13H0z M1.5 1.2l8 6 8-6v-.2h-16z" fill-rule="evenodd"/><path d="M0 0l9.5 7L19 0v1.4L9.5 8.4 0 1.4z" fill="#fff"/><path d="M0 13l7-6.4M19 13l-7-6.4" stroke="#fff" stroke-width="1.2"/></svg>
    <div class="contact abs" style="left:239px;top:137px;">email@firmdomain.com</div>

    <svg class="contact-icon" style="left:211px;top:183px;" width="18" height="18" viewBox="0 0 24 24" aria-hidden="true"><path d="M6.6 10.8a15 15 0 0 0 6.6 6.6l2.2-2.2a1 1 0 0 1 1-.25 11 11 0 0 0 3.6.6 1 1 0 0 1 1 1V20a1 1 0 0 1-1 1A17 17 0 0 1 3 4a1 1 0 0 1 1-1h3.5a1 1 0 0 1 1 1c0 1.25.2 2.45.6 3.6a1 1 0 0 1-.25 1z"/></svg>
    <div class="contact abs" style="left:239px;top:183px;">001 123 456 789</div>

    <div class="brand-panel">
      <div class="brand-name on-plum abs centered" style="left:0;width:316px;top:78px;">HARBOUR LANE LAW</div>
      <div class="web on-plum abs centered" style="left:0;width:316px;top:138px;">www.firmdomain.com</div>
      <span class="social social--light" role="img" aria-label="Professional network profile" style="left:80px;top:183px;"></span>
      <span class="social social--light" role="img" aria-label="Microblog profile" style="left:146px;top:183px;"></span>
      <span class="social social--light" role="img" aria-label="Social page" style="left:211px;top:183px;"></span>
    </div>
  </section>

  <!-- Centred layout with brand band -->
  <section class="signature signature--banner">
    <div class="person-name abs centered" style="left:0;width:845px;top:54px;">YOUR NAME</div>
    <div class="person-role abs centered" style="left:0;width:845px;top:95px;">LAWYER</div>

    <svg class="contact-icon" style="left:132px;top:146px;" width="19" height="13" viewBox="0 0 19 13" aria-hidden="true"><path d="M0 0h19v13H0z"/><path d="M0 0l9.5 7L19 0v1.4L9.5 8.4 0 1.4z" fill="#fff"/><path d="M0 13l7-6.4M19 13l-7-6.4" stroke="#fff" stroke-width="1.2"/></svg>
    <div class="contact abs" style="left:162px;top:141px;">email@firmdomain.com</div>

    <svg class="contact-icon" style="left:491px;top:143px;" width="18" height="18" viewBox="0 0 24 24" aria-hidden="true"><path d="M6.6 10.8a15 15 0 0 0 6.6 6.6l2.2-2.2a1 1 0 0 1 1-.25 11 11 0 0 0 3.6.6 1 1 0 0 1 1 1V20a1 1 0 0 1-1 1A17 17 0 0 1 3 4a1 1 0 0 1 1-1h3.5a1 1 0 0 1 1 1c0 1.25.2 2.45.6 3.6a1 1 0 0 1-.25 1z"/></svg>
    <div class="contact abs" style="left:519px;top:141px;">001 123 456 789</div>

    <div class="brand-band">
      <div class="brand-name on-plum abs centered" style="left:30px;width:240px;top:18px;">HARBOUR LANE LAW</div>
      <div class="web on-plum abs centered" style="left:314px;width:260px;top:23px;">www.firmdomain.com</div>
      <span class="social social--light" role="img" aria-label="Professional network profile" style="left:630px;top:20px;"></span>
      <span class="social social--light" role="img" aria-label="Microblog profile" style="left:695px;top:20px;"></span>
      <span class="social social--light" role="img" aria-label="Social page" style="left:760px;top:20px;"></span>
    </div>
  </section>

  <!-- Photo layout with footer rule -->
  <section class="signature signature--footer">
    <div class="headshot" role="img" aria-label="Head shot of the solicitor" style="left:50px;top:49px;width:110px;height:110px;"></div>
    <div class="person-name abs" style="left:195px;top:72px;">YOUR NAME</div>
    <div class="person-role abs" style="left:196px;top:113px;">LAWYER</div>

    <svg class="contact-icon" style="left:490px;top:70px;" width="19" height="13" viewBox="0 0 19 13" aria-hidden="true"><path d="M0 0h19v13H0z"/><path d="M0 0l9.5 7L19 0v1.4L9.5 8.4 0 1.4z" fill="#fff"/><path d="M0 13l7-6.4M19 13l-7-6.4" stroke="#fff" stroke-width="1.2"/></svg>
    <div class="contact abs" style="left:521px;top:66px;">email@firmdomain.com</div>

    <svg class="contact-icon" style="left:491px;top:113px;" width="18" height="18" viewBox="0 0 24 24" aria-hidden="true"><path d="M6.6 10.8a15 15 0 0 0 6.6 6.6l2.2-2.2a1 1 0 0 1 1-.25 11 11 0 0 0 3.6.6 1 1 0 0 1 1 1V20a1 1 0 0 1-1 1A17 17 0 0 1 3 4a1 1 0 0 1 1-1h3.5a1 1 0 0 1 1 1c0 1.25.2 2.45.6 3.6a1 1 0 0 1-.25 1z"/></svg>
    <div class="contact abs" style="left:521px;top:112px;">001 123 456 789</div>

    <div class="brand-rule"></div>
    <div class="brand-name in-plum abs centered" style="left:31px;width:240px;top:214px;">HARBOUR LANE LAW</div>
    <div class="web in-plum abs centered" style="left:314px;width:260px;top:219px;">www.firmdomain.com</div>
    <span class="social social--plum" role="img" aria-label="Professional network profile" style="left:634px;top:215px;"></span>
    <span class="social social--plum" role="img" aria-label="Microblog profile" style="left:699px;top:215px;"></span>
    <span class="social social--plum" role="img" aria-label="Social page" style="left:765px;top:215px;"></span>
  </section>
</body>
</html>
```